conférence Débat Innovation
Bonjour,
Dans le cadre de l'organisation d'un événement institutionnel, je suis à la recherche d'un professionnel graphiste pour la création des supports suivants :
- flyer de l'événement (pour web et print),
- version pour les réseaux sociaux et le site internet de l'événement,
- flyer de cet événement personnalisé pour un concours dont la finale aura lieu le jour de l'événement,
- version affiches pour le jour J,
- Carton d'invitation pour mailing et impression.
L'événement est une conférence débat sur l'entreprenariat et l'innovation en banlieue parisienne.
L'idée est de dynamiser un territoire et le mettre en avant ses atouts.

```html
<!DOCTYPE html>
<html lang="fr">
<head>
<meta charset="utf-8">
<title>Conférence / Débat – Entrepreunariat &amp; Innovation</title>
<link rel="stylesheet" href="https://fonts.googleapis.com/css2?family=Josefin+Sans:wght@100;300;400&family=Oswald:wght@500&display=swap">
<style>
  :root {
    --gold: #b98a2a;
    --teal: #1d8d9e;
    --ink: #2b2b2b;
    --white: #ffffff;
    --sky-warm: #cdbfae;
    --sky-grey: #b8bcbf;
    --glass-blue: #7fa4bd;
    --glass-deep: #4f7590;
  }
  html, body { margin: 0; padding: 0; overflow: hidden; background: #ffffff; }
  .poster {
    position: relative;
    width: 839px;
    height: 1200px;
    overflow: hidden;
    font-family: "Josefin Sans", sans-serif;
  }
  .poster__shapes { position: absolute; inset: 0; }
  .poster__text { position: absolute; margin: 0; white-space: nowrap; line-height: 1; }

  .event-type {
    top: 60px; left: 0; width: 839px; text-align: center;
    font-weight: 300; font-size: 34px; letter-spacing: 12px; color: var(--ink);
  }
  .title-main {
    top: 352px; left: 106px; width: 315px; text-align: center;
    font-weight: 300; font-size: 30px; color: var(--white);
  }
  .title-amp {
    top: 384px; left: 126px;
    font-weight: 100; font-size: 140px; color: var(--white);
  }
  .title-second {
    top: 434px; left: 204px;
    font-weight: 300; font-size: 33px; color: var(--white);
  }
  .venue {
    top: 540px; left: 116px; width: 359px; text-align: center;
    font-family: "Oswald", sans-serif; font-weight: 500; font-size: 23px;
    letter-spacing: 3.5px; color: var(--ink); line-height: 39px;
  }
  .city {
    top: 596px; left: 116px; width: 359px; text-align: center;
    font-family: "Oswald", sans-serif; font-weight: 500; font-size: 34px;
    letter-spacing: 9px; color: var(--white); line-height: 46px;
  }
  .date-day {
    top: 236px; left: 566px;
    font-weight: 100; font-size: 128px; color: var(--teal); letter-spacing: 22px;
  }
  .date-year {
    top: 306px; left: 680px;
    font-weight: 300; font-size: 22px; color: var(--teal); letter-spacing: 3px;
    transform: rotate(-90deg); transform-origin: left top;
  }
  .date-month {
    top: 346px; left: 574px;
    font-weight: 300; font-size: 46px; color: var(--teal); letter-spacing: 8px;
  }
  .tagline-claim {
    top: 820px; left: 236px; width: 520px; text-align center;
    text-align: center;
    font-weight: 300; font-size: 26px; color: var(--teal);
    transform: rotate(-3deg);
  }
  .tagline-invite {
    top: 876px; left: 200px; width: 540px;
    text-align: center;
    font-weight: 300; font-size: 25px; color: var(--white);
    transform: rotate(-3deg);
  }
  .logo-slot {
    position: absolute; top: 1058px; left: 345px; width: 188px; height: 111px;
    background: var(--white);
    display: flex; align-items: center; justify-content: center;
    font-family: "Josefin Sans", sans-serif; font-weight: 400; font-size: 24px; color: var(--ink);
  }
</style>
</head>
<body>
<main class="poster">
  <svg class="poster__shapes" width="839" height="1200" viewBox="0 0 839 1200">
    <defs>
      <linearGradient id="sky" x1="0" y1="0" x2="1" y2="0.3">
        <stop offset="0" stop-color="var(--sky-warm)"/>
        <stop offset="0.45" stop-color="var(--sky-grey)"/>
        <stop offset="0.75" stop-color="var(--glass-blue)"/>
        <stop offset="1" stop-color="var(--glass-deep)"/>
      </linearGradient>
    </defs>
    <rect class="backdrop-photo" role="img" aria-label="Photo en contre-plongée d'une tour de bureaux en verre reflétant un ciel nuageux" x="0" y="0" width="839" height="1200" fill="url(#sky)"/>

    <polygon class="hex-title" points="57,460 159,239 428,239 532,460 428,682 159,682" fill="var(--gold)" opacity="0.92"/>
    <polygon class="hex-date" points="528,304 587,176 746,176 802,304 746,429 587,429" fill="var(--white)" opacity="0.93"/>

    <line class="title-rule" x1="175" y1="316" x2="420" y2="316" stroke="var(--white)" stroke-width="3" stroke-dasharray="3 5"/>
    <line class="title-rule" x1="175" y1="500" x2="420" y2="500" stroke="var(--white)" stroke-width="3" stroke-dasharray="3 5"/>
    <rect class="venue-bar" x="116" y="540" width="359" height="39" fill="var(--white)"/>

    <polygon class="ribbon-light" points="5,701 790,800 790,850 230,872" fill="var(--white)"/>
    <polygon class="ribbon-teal" points="183,878 790,850 780,902 215,932" fill="var(--teal)"/>
  </svg>

  <p class="poster__text event-type">CONFÉRENCE / DÉBAT</p>

  <p class="poster__text title-main">ENTREPREUNARIAT</p>
  <p class="poster__text title-amp">&amp;</p>
  <p class="poster__text title-second">INNOVATION</p>
  <p class="poster__text venue">PALAIS DES RENCONTRES</p>
  <p class="poster__text city">PARIS</p>

  <p class="poster__text date-day">21</p>
  <p class="poster__text date-year">2016</p>
  <p class="poster__text date-month">SEPT</p>

  <p class="poster__text tagline-claim">LA BANLIEU EST PLEINE DE RESSOURCES !</p>
  <p class="poster__text tagline-invite">VENEZ PARTAGER VOS EXPÉRIENCES</p>

  <div class="logo-slot">LOGO</div>
</main>
</body>
</html>
```